Tavrelo.com.au - AV and Communications Installation Company Website

A company website for a modern, high level/enterprise communications installation/engineering company based in Sydney Australia.
My client base is construction companies working in medical, government and educations departments so the website needs to look professional.
Clients like Quenby or Dorvik as I want to eventually move into data centre design and installation so I need something appealing to the high end market.
Fiber Optic Installation is a massive part of the company aswell.
Audio visual, IT installation is also what the company will be involved in.
I want the website to be modern, eye catching, professional looking.

Target Market(s)

High end clients and construction companies

Industry/Entity Type

Communications

Coding

Coded - Design and coding required

Number of Pages Required

1 page

Requirements
Must have
• Modern and clean layout with links to other social media platforms

```html
<!DOCTYPE html>
<html lang="en">
<head>
<meta charset="utf-8">
<title>Tavrelo – Communications Installation</title>
<link href="https://fonts.googleapis.com/css2?family=Inter:ital,wght@0,300;0,400;0,600;0,700;0,800;1,900&display=swap" rel="stylesheet">
<style>
:root{
  --teal:#1e8797;
  --ink:#111;
  --text:#2b2b2b;
  --muted:#6c6c6c;
  --light:#efefef;
  --panel:#e4e4e4;
  --menu:#6a6a6a;
  --bar:#6b6b70;
  --white:#fff;
  --num:#c9d0bf;
}
*{margin:0;padding:0;box-sizing:border-box}
html,body{width:1200px;height:3196px;overflow:hidden}
body{position:relative;background:var(--white);font-family:"Inter",Helvetica,Arial,sans-serif;color:var(--text)}
.abs{position:absolute}
.wordmark{font-size:40px;font-weight:600;color:var(--teal);letter-spacing:1px;display:flex;align-items:center;gap:10px}
.wordmark .dot{width:16px;height:16px;background:var(--teal)}
/* header */
.site-header{left:0;top:0;width:1200px;height:105px;background:var(--white);box-shadow:0 2px 4px rgba(0,0,0,.08);z-index:3}
.site-header .wordmark{position:absolute;left:96px;top:30px}
.nav a{position:absolute;top:41px;font-size:16px;font-weight:300;color:#555;text-decoration:none;white-space:nowrap}
.nav a.active{color:var(--teal);font-weight:600}
.dropdown{left:805px;top:92px;width:257px;z-index:4}
.dropdown div{height:36px;background:var(--menu);color:var(--white);font-size:13.5px;padding:11px 15px;border-bottom:1px solid #8a8a8a}
/* hero */
.hero{left:0;top:105px;width:1200px;height:400px;background:var(--light)}
.hero-art{left:422px;top:105px;width:778px;height:400px;background:linear-gradient(110deg,#efefef 10%,#c9c9c4 45%,#e6d24a 62%,#2a2a2a 85%)}
.hero-title{left:96px;top:232px;font-size:60px;font-weight:900;font-style:italic;color:var(--ink);line-height:1}
.hero-sub{left:96px;top:282px;font-size:40px;font-weight:300;color:#333;line-height:1}
.btn{display:flex;align-items:center;justify-content:center;background:var(--ink);color:var(--white);border-radius:22px;font-weight:600}
.hero-btn{left:96px;top:340px;width:96px;height:30px;font-size:13px}
.arrow{top:292px}
/* sections */
.section-title{font-size:50px;color:var(--ink);font-weight:400;letter-spacing:-.5px;text-align:center;width:1200px;left:0}
.section-title b{font-weight:800}
.about-title{left:96px;top:596px;font-size:50px;color:var(--ink);letter-spacing:-.5px}
.about-title b{font-weight:800}
.about-text{left:94px;top:700px;width:630px;font-size:15.3px;line-height:25px;color:#222}
.about-art{left:770px;top:505px;width:330px;height:340px;background:linear-gradient(160deg,#f2e25a 0%,#ffffff 30%,#2e6fc0 55%,#8fb4e0 100%);border-radius:8px}
.services{left:0;top:918px;width:1200px;height:559px;background:linear-gradient(135deg,#dedede,#ececec 50%,#d9d9d9)}
.service{width:320px;text-align:center}
.service .num{font-size:150px;font-weight:800;color:var(--num);line-height:1;position:absolute;left:0;width:320px;top:-128px;opacity:.75}
.service h3{position:relative;font-size:18px;font-weight:400;color:var(--ink);margin-bottom:8px}
.service p{position:relative;font-size:12.5px;line-height:20.5px;color:#666}
.services-btn{left:525px;top:1339px;width:150px;height:37px;font-size:15px;font-weight:400}
.client{top:1715px;width:140px;height:104px;background:var(--light);font-size:21px;color:var(--ink);display:flex;align-items:center;justify-content:center}
.contact{left:0;top:1921px;width:1200px;height:675px;background:linear-gradient(160deg,#d9d9d9,#e8e8e8 55%,#d4d4d4)}
.field{background:#f6f6f6;border:1px solid #b8b8b8;border-radius:22px;font-size:13px;color:#777;padding:0 22px;display:flex;align-items:center}
.field.area{border-radius:22px;align-items:flex-start;padding-top:18px}
.submit{left:536px;top:2458px;width:127px;height:38px;font-size:13px}
/* footer */
.footer-text{left:96px;top:2767px;width:240px;font-size:14.5px;line-height:21.5px;color:#444}
.col-title{top:2681px;font-size:17.5px;font-weight:600;color:var(--ink)}
.col-rule{top:2717px;width:102px;height:2px;background:var(--teal)}
.link{left:391px;font-size:14.5px;color:#444;display:flex;align-items:center;gap:16px}
.link::before{content:"";width:12px;height:2px;background:var(--teal)}
.label{left:607px;font-size:14px;font-weight:600;color:var(--teal)}
.info{left:607px;font-size:14.5px;color:#444;line-height:20px}
.contact-line{left:866px;font-size:14.5px;color:#444;line-height:20px;display:flex;gap:12px}
.contact-line svg{flex:none;margin-top:3px}
.bottom-bar{left:0;top:3100px;width:1200px;height:96px;background:var(--bar);color:var(--white);font-size:13.5px;font-weight:600;display:flex;align-items:center;justify-content:center}
</style>
</head>
<body>

<header class="abs site-header">
  <div class="wordmark"><span class="dot"></span>Tavrelo</div>
  <nav class="nav">
    <a class="active" style="left:606px">Home</a>
    <a style="left:695px">About Us</a>
    <a style="left:809px">Our Services -</a>
    <a style="left:957px">Clients</a>
    <a style="left:1049px">Contact</a>
  </nav>
</header>
<div class="abs dropdown"><div>Fibre Optics</div><div>Audio Visual</div><div>IT Installation</div></div>

<section class="abs hero"></section>
<div class="abs hero-art" role="img" aria-label="Close-up photo of a fibre optic cable with coloured strands"></div>
<div class="abs hero-title">Fastest</div>
<div class="abs hero-sub">than you think</div>
<div class="abs btn hero-btn">Read more</div>
<svg class="abs arrow" style="left:34px" width="28" height="22" viewBox="0 0 28 22"><path d="M26 11H4M12 3L4 11l8 8" fill="none" stroke="#111" stroke-width="4"/></svg>
<svg class="abs arrow" style="left:1138px" width="28" height="22" viewBox="0 0 28 22"><path d="M2 11h22M16 3l8 8-8 8" fill="none" stroke="#111" stroke-width="4"/></svg>

<h2 class="abs about-title"><b>About</b> Us</h2>
<p class="abs about-text">Lorem ipsum dolor sit amet, consectetur adipiscing elit. Vivamus vitae purus non magna porttitor sodales. Ut id porttitor sapien. Aliquam ex ligula, condimentum ac sapien ut, convallis vestibulum ante. Morbi mollis eros in tincidunt dapibus. Curabitur velit eros, vulputate eu aliquet quis, laoreet ac ligula. Etiam viverra lorem eget eleifend malesuada. Integer aliquet in mi id tempor. Suspendisse mollis bibendum facilisis.</p>
<div class="abs about-art" role="img" aria-label="Photo of yellow fibre patch cables with blue SC connectors"></div>

<section class="abs services" role="img" aria-label="Faded photo of a circuit board"></section>
<h2 class="abs section-title" style="top:1010px"><b>Our</b> Services</h2>
<div class="abs service" style="left:92px;top:1205px"><div class="num">1</div><h3>Fibre Optics</h3><p>Lorem ipsum dolor sit amet, consectetur adipiscing elit. Nullam pellentesque purus nisi, sed cursus purus laoreet ut. Quisque vulputate turpis eu dolor suscipit luctus.</p></div>
<div class="abs service" style="left:441px;top:1205px"><div class="num">2</div><h3>Audio Visual</h3><p>Lorem ipsum dolor sit amet, consectetur adipiscing elit. Nullam pellentesque purus nisi, sed cursus purus laoreet ut. Quisque vulputate turpis eu dolor suscipit luctus.</p></div>
<div class="abs service" style="left:794px;top:1205px"><div class="num">3</div><h3>IT Installation</h3><p>Lorem ipsum dolor sit amet, consectetur adipiscing elit. Nullam pellentesque purus nisi, sed cursus purus laoreet ut. Quisque vulputate turpis eu dolor suscipit luctus.</p></div>
<div class="abs btn services-btn">View in details</div>

<h2 class="abs section-title" style="top:1570px;left:-10px"><b>Our</b> Clients</h2>
<div class="abs client" style="left:96px">Client1 img</div>
<div class="abs client" style="left:302px">Client2 img</div>
<div class="abs client" style="left:532px">Client3 img</div>
<div class="abs client" style="left:760px">Client4 img</div>
<div class="abs client" style="left:967px">Client5 img</div>

<section class="abs contact" role="img" aria-label="Faded photo of a mixing console"></section>
<h2 class="abs section-title" style="top:1976px;left:25px"><b>Contact</b> Us</h2>
<div class="abs field" style="left:383px;top:2092px;width:204px;height:44px">Name *</div>
<div class="abs field" style="left:613px;top:2092px;width:203px;height:44px">Mobile</div>
<div class="abs field" style="left:383px;top:2160px;width:204px;height:44px">Email *</div>
<div class="abs field" style="left:613px;top:2160px;width:203px;height:44px;justify-content:space-between">Choose a Service *<svg width="10" height="6"><path d="M0 0h10L5 6z" fill="#333"/></svg></div>
<div class="abs field area" style="left:383px;top:2231px;width:433px;height:201px">Message *</div>
<div class="abs btn submit">Submit</div>

<div class="abs wordmark" style="left:96px;top:2682px"><span class="dot"></span>Tavrelo</div>
<p class="abs footer-text">Lorem ipsum dolor sit amet, consectetur adipiscing elit. Nullam pellentesque purus nisi, sed cursus purus laoreet ut. Quisque vulputate turpis eu dolor suscipit luctus. Vivamus non lorem vitae erat pretium rutrum. Sed sit amet viverra neque. Nulla egestas ligula vitae urna imperdiet venenatis. Donec cursus dictum neque ut euismod. Sed gravida lobortis lacinia.</p>

<div class="abs col-title" style="left:391px">Useful Links</div><div class="abs col-rule" style="left:391px"></div>
<div class="abs link" style="top:2765px">Home</div>
<div class="abs link" style="top:2823px">About Us</div>
<div class="abs link" style="top:2880px">Our Services</div>
<div class="abs link" style="top:2938px">Clients</div>
<div class="abs link" style="top:2996px">Contact</div>

<div class="abs col-title" style="left:607px">About Us</div><div class="abs col-rule" style="left:607px"></div>
<div class="abs label" style="top:2766px">Timings</div>
<div class="abs info" style="top:2796px">Mon-Fri: 8:00am - 04:30pm<br>Sat-Sun &amp; Holidays: Closed</div>
<div class="abs label" style="top:2861px">Service</div>
<div class="abs info" style="top:2891px">Lorem ipsum</div>
<div class="abs label" style="top:2938px">Tavrelo</div>
<div class="abs info" style="top:2968px">Lorem ipsum</div>

<div class="abs col-title" style="left:865px">Contact Info</div><div class="abs col-rule" style="left:865px"></div>
<div class="abs contact-line" style="top:2766px"><svg width="15" height="11" viewBox="0 0 15 11"><rect width="15" height="11" fill="var(--teal)"/><path d="M1 1l6.5 5L14 1" fill="none" stroke="#fff" stroke-width="1.3"/></svg>info@tavrelo.com.au</div>
<div class="abs contact-line" style="top:2806px"><svg width="14" height="14" viewBox="0 0 14 14"><path d="M3 1l2.5 3-1.5 1.5c1 2 2.5 3.5 4.5 4.5L10 8.5l3 2.5-1.5 2C6 13 1 8 1 2.5z" fill="var(--teal)"/></svg>123-456-7899</div>
<div class="abs contact-line" style="top:2846px"><svg width="12" height="15" viewBox="0 0 12 15"><path d="M6 0a6 6 0 0 0-6 6c0 4 6 9 6 9s6-5 6-9a6 6 0 0 0-6-6z" fill="var(--teal)"/><circle cx="6" cy="6" r="2.2" fill="#fff"/></svg><span>50158 Lorem ipsum<br>#451, Lorem, AB Lorem<br>ipsum, dolor</span></div>

<footer class="abs bottom-bar">Copyright © 2020. All Rights Reserved</footer>

</body>
</html>
```